Herbal Tincture Product Packaging

Rebrand herbal product labels for use on 2 oz tincture bottles - current packaging attached. (no box needed). Bottles are frosted glass Boston rounds 2 oz with silver cap dropper. logo options attached. 3 products/varieties: Harbor, Lantern, Meadow - would really also like a visual icon to represent product variety at a glance, in addition to name.
Please see guidelines below:
Label Material:
Base- polyester, BOPP, or other non-vinyl synthetics Lamination- matte or gloss Backing- white or kraft, no transparent
Spooling:
Rewind direction #4, 3” core, not more that 1200 per roll, not less than 500 per roll Please include 5-10% overage (ex. if you have 500 units on order, please print 525-550 labels).
Sizing:
2oz. ABR- >/= 2” H x 4.5” W
Suggested guidelines review:
https://www.krvl.org/files/Document%20Library/KRVL%20Guidance%20Documents/Packaging%20and%20Labeling/KRVL%20Guidance_Herbal%20Supplements%20Labeling%20Guide%20(Revised%202021).pdf
Target Market(s)
Health Conscious age 24+
Industry/Entity Type
holistic health care
Colors
Look and feel

```html
<!DOCTYPE html>
<html lang="en">
<head>
<meta charset="utf-8">
<title>Harbor – Herbal Support Label</title>
<link href="https://fonts.googleapis.com/css2?family=Cinzel:wght@400;700&family=Libre+Baskerville:wght@700&family=Arimo:wght@400&display=swap" rel="stylesheet">
<style>
  :root {
    --lavender-bg: #ece8f3;
    --lavender-soft: #f6f3fa;
    --lavender-pattern: #ddd5ea;
    --purple: #5f2a86;
    --purple-deep: #4a1c6c;
    --purple-light: #7a3ea3;
    --gold: #c9ad7a;
    --gold-light: #e7d6ae;
    --ornament: #d8c9b0;
    --green: #2f8a3e;
    --white: #ffffff;
    --silver: #d9d9e0;
  }
  * { margin: 0; padding: 0; box-sizing: border-box; }
  html, body { width: 1200px; height: 533px; overflow: hidden; }
  body { background: var(--lavender-bg); }

  .label {
    position: relative;
    width: 1200px;
    height: 533px;
    overflow: hidden;
    background: var(--lavender-bg);
  }
  .background-pattern {
    position: absolute; inset: 0;
    background: radial-gradient(circle at 50% 50%, var(--lavender-soft) 0%, var(--lavender-bg) 60%, var(--lavender-pattern) 100%);
  }
  .ornament {
    position: absolute;
    width: 460px; height: 460px;
    top: 37px;
    border-radius: 50%;
    background: radial-gradient(circle, rgba(216,201,176,0.15) 0%, rgba(216,201,176,0.55) 55%, rgba(216,201,176,0.25) 75%, rgba(216,201,176,0) 100%);
  }
  .ornament--left { left: 214px; }
  .ornament--right { left: 526px; }

  .band {
    position: absolute;
    left: 459px; top: 0;
    width: 284px; height: 533px;
    background: linear-gradient(90deg, var(--purple-deep) 0%, var(--purple) 20%, var(--purple-light) 50%, var(--purple) 80%, var(--purple-deep) 100%);
    border-left: 3px solid var(--gold);
    border-right: 3px solid var(--gold);
    box-shadow: 0 0 0 2px rgba(255,255,255,0.35);
  }

  .badge {
    position: absolute;
    left: 601px; top: 245px;
    width: 300px; height: 300px;
    margin: -150px 0 0 -150px;
    border-radius: 50%;
    background: radial-gradient(circle at 50% 40%, var(--purple-light) 0%, var(--purple) 60%, var(--purple-deep) 100%);
    border: 5px solid var(--gold);
    box-shadow: 0 0 0 2px var(--gold-light), 0 4px 12px rgba(40,10,60,0.45);
    color: var(--white);
    text-align: center;
  }
  .brand-mark {
    position: absolute;
    left: 601px; top: 89px;
    width: 118px; height: 118px;
    margin: -59px 0 0 -59px;
    border-radius: 50%;
    background: var(--green);
    border: 5px solid var(--white);
    box-shadow: 0 2px 6px rgba(40,10,60,0.4);
  }
  .brand-name {
    position: absolute;
    top: 58px; left: 0; right: 0;
    font-family: "Cinzel", serif;
    font-weight: 400;
    font-size: 19px;
    letter-spacing: 3px;
    line-height: 1.15;
    color: var(--white);
  }
  .rule {
    position: absolute;
    left: 30px; right: 30px;
    height: 2px;
    background: linear-gradient(90deg, transparent, var(--gold-light), var(--gold), var(--gold-light), transparent);
  }
  .rule--top { top: 118px; }
  .rule--bottom { top: 198px; }
  .product-name {
    position: absolute;
    top: 126px; left: 0; right: 0;
    font-family: "Libre Baskerville", serif;
    font-weight: 700;
    font-size: 56px;
    letter-spacing: 1px;
    color: var(--silver);
    text-shadow: 0 2px 3px rgba(20,0,40,0.6);
  }
  .formats {
    position: absolute;
    top: 210px; left: 0; right: 0;
    font-family: "Arimo", sans-serif;
    font-size: 18px;
    letter-spacing: 0.5px;
    color: var(--white);
  }
  .tagline {
    position: absolute;
    top: 240px; left: 0; right: 0;
    font-family: "Arimo", sans-serif;
    font-size: 22px;
    color: var(--gold-light);
  }
  .volume {
    position: absolute;
    left: 459px; width: 284px;
    top: 470px;
    text-align: center;
    font-family: "Arimo", sans-serif;
    font-size: 24px;
    color: var(--white);
  }
</style>
</head>
<body>
  <main class="label">
    <div class="background-pattern" role="img" aria-label="Soft lavender lace damask pattern"></div>
    <div class="ornament ornament--left" role="img" aria-label="Gold mandala ornament"></div>
    <div class="ornament ornament--right" role="img" aria-label="Gold mandala ornament"></div>

    <div class="band"></div>

    <section class="badge">
      <p class="brand-name">KESTREL<br>WELLNESS</p>
      <div class="rule rule--top"></div>
      <h1 class="product-name">HARBOR</h1>
      <div class="rule rule--bottom"></div>
      <p class="formats">TEAS | TONICS | TINCTURES</p>
      <p class="tagline">Herbal Support</p>
    </section>

    <div class="brand-mark"></div>

    <p class="volume">2oz | 60ml</p>
  </main>
</body>
</html>
```